Business Cards Design for the electrical wholesaler: clean bold dynamic :)

We need a business card design that would follow our latest brand guidelines. As an electrical wholesaler we want to bring a fresh look and feel into the industry. The design should be clean bold and dynamic. It should come alive with the renewed energy of our green colour. Our grey colour should keep things balanced and complement the notion of maturity and responsibility. We employ Lato as a corporate font however are not bound by this font and we’re open to interpretation here.

Target Market(s)

Electrical contractors

Industry/Entity Type

Business

Contact Information for Business Card

Logo
Name & Surname: Olena Dovbush
Job Title: Director of Marketing
Email: helen.dovbush@mailvane.example
Cell phone: XXX.XXX.XXXX
Address: 20917 - 87 Ave. Edmonton, AB, Canada. T6K 2R8
Business Phone: 780.555.0187
Website: www.qorvil.example

Font styles to use
Other font styles liked:
• Lato

Requirements
Must have
• Logo & website
Nice to have
• Brand elements - some of them you may find in the attached Brand Guidelines (e.g. three lines on the background signifying "W")

```html
<!DOCTYPE html>
<html lang="en">
<head>
<meta charset="utf-8">
<title>Qorvil business cards</title>
<link href="https://fonts.googleapis.com/css2?family=Lato:wght@400;700;900&display=swap" rel="stylesheet">
<style>
  :root {
    --green: #8cc63f;
    --grey: #4a4a4c;
    --ink: #1e1e1e;
    --paper: #ffffff;
    --stage: #2b2b2b;
  }
  * { box-sizing: border-box; margin: 0; padding: 0; }
  html, body { width: 1200px; height: 900px; overflow: hidden; }
  body {
    background: var(--stage);
    font-family: "Lato", Arial, sans-serif;
    color: var(--ink);
    position: relative;
  }
  .card {
    position: absolute;
    left: 250px;
    width: 700px;
    height: 400px;
    background: var(--paper);
    border-radius: 22px;
    box-shadow: 0 10px 30px rgba(0,0,0,.5);
    overflow: hidden;
  }
  .card--front { top: 35px; }
  .card--back { top: 465px; }

  .brand {
    display: flex;
    align-items: center;
    gap: 14px;
  }
  .brand__mark {
    background: var(--green);
    border-radius: 4px;
  }
  .brand__name {
    font-weight: 700;
    color: var(--grey);
    letter-spacing: -1px;
    line-height: 1;
  }

  .card--front .brand {
    position: absolute;
    left: 0; right: 0; top: 140px;
    justify-content: center;
  }
  .card--front .brand__mark { width: 58px; height: 58px; }
  .card--front .brand__name { font-size: 88px; }
  .front__web {
    position: absolute;
    left: 0; right: 0; bottom: 48px;
    text-align: center;
    font-size: 19px;
    color: var(--ink);
  }

  .card--back .brand { position: absolute; left: 44px; top: 50px; }
  .card--back .brand__mark { width: 40px; height: 40px; }
  .card--back .brand__name { font-size: 58px; }

  .address {
    position: absolute;
    right: 44px; top: 118px;
    text-align: right;
    font-size: 16px;
    line-height: 1.3;
  }
  .rule {
    position: absolute;
    left: 44px; right: 44px; top: 178px;
    height: 3px;
    background: var(--green);
  }
  .person { position: absolute; left: 44px; top: 124px; }
  .person__name {
    font-size: 24px;
    font-weight: 700;
    color: var(--green);
    line-height: 1.1;
  }
  .person__title { font-size: 17px; color: var(--ink); }

  .contacts {
    position: absolute;
    left: 44px; top: 206px;
    list-style: none;
  }
  .contacts__item {
    display: flex;
    align-items: center;
    gap: 14px;
    height: 38px;
    font-size: 20px;
  }
  .contacts__icon {
    width: 30px; height: 30px;
    background: var(--green);
    display: flex; align-items: center; justify-content: center;
  }
</style>
</head>
<body>

<section class="card card--front">
  <div class="brand">
    <span class="brand__mark"></span>
    <span class="brand__name">Qorvil</span>
  </div>
  <p class="front__web">www.qorvil.example</p>
</section>

<section class="card card--back">
  <div class="brand">
    <span class="brand__mark"></span>
    <span class="brand__name">Qorvil</span>
  </div>

  <p class="address">20917 - 87 Ave. Edmonton, AB,<br>Canada. T6K 2R8</p>

  <div class="person">
    <p class="person__name">Olena Dovbush</p>
    <p class="person__title">Director of Marketing</p>
  </div>

  <div class="rule"></div>

  <ul class="contacts">
    <li class="contacts__item">
      <span class="contacts__icon">
        <svg width="18" height="18" viewBox="0 0 24 24"><path fill="#fff" d="M6.6 10.8a15 15 0 0 0 6.6 6.6l2.2-2.2c.3-.3.7-.4 1-.2 1.1.4 2.3.6 3.6.6.6 0 1 .4 1 1V20c0 .6-.4 1-1 1A17 17 0 0 1 3 4c0-.6.4-1 1-1h3.5c.6 0 1 .4 1 1 0 1.3.2 2.5.6 3.6.1.3 0 .7-.2 1z"/></svg>
      </span>
      780.555.0142
    </li>
    <li class="contacts__item">
      <span class="contacts__icon">
        <svg width="18" height="18" viewBox="0 0 24 24"><path fill="#fff" d="M3 8c3-3 15-3 18 0v3h-4V9H7v2H3zM6 12h12l2 8H4zM12 14a2.5 2.5 0 1 0 0 5 2.5 2.5 0 0 0 0-5z"/></svg>
      </span>
      780.555.0187
    </li>
    <li class="contacts__item">
      <span class="contacts__icon">
        <svg width="18" height="18" viewBox="0 0 24 24"><path fill="none" stroke="#fff" stroke-width="2" d="M3 6h18v12H3zM3 6l9 7 9-7"/></svg>
      </span>
      helen.dovbush@mailvane.example
    </li>
    <li class="contacts__item">
      <span class="contacts__icon">
        <svg width="18" height="18" viewBox="0 0 24 24"><g fill="none" stroke="#fff" stroke-width="2"><circle cx="12" cy="12" r="9"/><path d="M3 12h18M12 3c3 3 3 15 0 18M12 3c-3 3-3 15 0 18"/></g></svg>
      </span>
      www.qorvil.example
    </li>
  </ul>
</section>

</body>
</html>
```